Brellin Trade Partners - we are Asian sourcing agents

We are sourcing agents based in the USA and we act as sourcing agents for clients in throughout the world. We focus primarily on custom sewn goods. So basically companies who do not have the in-house expertise to do it themselves, come to us and have us find suitable factories in Asia to do the production. We are middlemen. We find the factories...quote the project...manage the quality control and then deliver the goods directly to our customer's door. We pride ourselves in making the communication very easy and precise.

Current page is www.brellintrade.example

I am not happy w/ the overall look. The spacing...the photos, the fonts...the design elements...the pictures. I want a cool, crisp design that conveys professionalism and clearly depicts/explains what we do.

Requirements
Must have
• use my logo....I like it...it was designed by someone on this website.
Nice to have
• a video/animation of the entire process would be wonderful. Showing initial contact with our office in the USA...then to my correspondence with my offices in Taiwan and in Hong Kong...and then back and fort w/ the customer.....and then between my people in Hong Kong/Taiwan with the local factories......and then a quote is generated and sent to my client......to samples being made and sent for approval.....to a PO being generated......to final samples being sent.....to the order being shipped and delivered to the clients warehouse. I was thinking of an animation showing arrows and text showing the back and forth communication and explaining how the process flows.

```html
<!DOCTYPE html>
<html lang="en">
<head>
<meta charset="utf-8">
<title>Brellin Trade Partners – Asian Sourcing Agents</title>
<link rel="stylesheet" href="https://fonts.googleapis.com/css2?family=Open+Sans:wght@400;600;700;800&display=swap">
<style>
:root{
  --navy:#0f1f5c;
  --navy-line:#2a3a78;
  --green:#5b8a1b;
  --grey-band:#e6e6e6;
  --grey-box:#ececec;
  --grey-label:#3d3d3d;
  --text:#222;
  --text-soft:#444;
  --footer-text:#aab3d4;
  --white:#fff;
}
*{box-sizing:border-box;margin:0;padding:0}
html,body{width:1200px;height:2367px;overflow:hidden}
body{position:relative;font-family:"Open Sans",sans-serif;color:var(--text);background:var(--white)}
.abs{position:absolute}

/* header */
.site-header{left:0;top:0;width:1200px;height:116px;background:linear-gradient(#fdfdfd,#ececec)}
.brand{left:185px;top:38px;display:flex;align-items:center;gap:12px}
.brand-mark{width:24px;height:24px;background:var(--navy)}
.brand-name{font-weight:800;font-size:30px;line-height:1;color:var(--navy);letter-spacing:.5px}
.header-phone{left:866px;top:45px;display:flex;align-items:center;gap:8px;font-size:22px;color:#111}

/* nav */
.main-nav{left:0;top:116px;width:1200px;height:38px;background:var(--navy)}
.nav-list{list-style:none;display:flex;position:absolute;left:185px;top:0;height:38px}
.nav-list li{height:38px;display:flex;align-items:center;padding:0 28px;color:var(--white);font-size:15px;border-left:1px solid var(--navy-line)}
.nav-list li:first-child{border-left:none}
.nav-list li.is-active{background:var(--green);padding:0 22px;height:28px;margin-top:5px;margin-right:14px}

/* hero */
.hero-photo{left:0;top:154px;width:1200px;height:341px;
  background:
    radial-gradient(ellipse 260px 200px at 200px 230px,rgba(120,170,150,.85),transparent 70%),
    radial-gradient(ellipse 220px 160px at 1080px 120px,rgba(60,70,80,.8),transparent 70%),
    radial-gradient(ellipse 300px 120px at 560px 290px,rgba(200,205,200,.9),transparent 70%),
    linear-gradient(110deg,#7f9a92 0%,#b8c4bf 38%,#8d9aa0 62%,#5e6b72 100%)}
.hero-caption{left:703px;top:296px;width:331px;height:88px;background:rgba(255,255,255,.94);box-shadow:0 6px 10px rgba(0,0,0,.35);padding:6px 10px;font-size:34px;line-height:38px;color:#222}

/* intro band */
.intro-band{left:0;top:495px;width:1200px;height:232px;background:var(--grey-band);border-top:2px dotted #9a9a9a}
.section-title{font-weight:700;font-size:23px;color:#111;letter-spacing:.2px}
.intro-title{left:165px;top:528px}
.intro-copy{left:165px;top:568px;width:395px;font-size:13px;line-height:17.5px;color:var(--text-soft)}
.video-frame{left:590px;top:527px;width:442px;height:236px;background:#111;box-shadow:0 6px 12px rgba(0,0,0,.35);border:6px solid #fff}
.video-still{left:0;top:0;width:430px;height:224px;
  background:
    radial-gradient(ellipse 120px 90px at 90px 150px,rgba(210,190,170,.7),transparent 70%),
    radial-gradient(ellipse 140px 90px at 330px 110px,rgba(90,110,140,.7),transparent 70%),
    linear-gradient(135deg,#56646f,#98a4aa 50%,#465460)}
.video-title{left:8px;top:4px;font-size:10px;color:#ddd}
.video-play{left:185px;top:82px;width:60px;height:60px;border-radius:50%;background:rgba(0,0,0,.65)}
.video-controls{left:0;top:206px;width:430px;height:18px;background:rgba(0,0,0,.8)}
.video-progress{left:8px;top:8px;width:414px;height:3px;background:#555}

/* products */
.sourcing-title{left:165px;top:793px}
.sourcing-copy{left:165px;top:832px;width:870px;font-size:13px;line-height:17.5px;color:var(--text-soft)}
.product-card{width:188px;height:210px;background:var(--white);border:1px solid #ddd;box-shadow:0 8px 10px -4px rgba(0,0,0,.35)}
.product-photo{position:absolute;left:12px;top:12px;width:162px;height:146px}
.product-label{position:absolute;left:12px;top:158px;width:162px;height:36px;background:var(--grey-label);color:var(--white);font-weight:700;font-size:16px;display:flex;align-items:center;justify-content:center}

/* contact band */
.contact-band{left:0;top:1413px;width:1200px;height:327px;background:var(--grey-band);border-top:2px dotted #9a9a9a;border-bottom:2px dotted #9a9a9a}
.contact-lead{left:185px;top:1488px;width:430px;font-size:20px;line-height:30px;color:#111}
.contact-lines{left:185px;top:1572px;font-size:19px;line-height:30px;color:#111}
.quote-form{left:691px;top:1449px;width:327px;height:326px;background:var(--white);box-shadow:0 4px 10px rgba(0,0,0,.3)}
.quote-head{height:48px;background:var(--navy);color:var(--white);font-weight:700;font-size:21px;padding:10px 24px}
.quote-field{position:absolute;left:24px;width:280px;height:36px;border:1px solid #bbb;font-size:14px;color:#888;padding:8px 10px}
.quote-submit{position:absolute;left:234px;top:278px;width:68px;height:28px;background:var(--navy);color:var(--white);font-size:14px;display:flex;align-items:center;justify-content:center}

/* link panels */
.link-panel{top:1813px;width:426px;height:220px;background:var(--grey-box)}
.link-head{height:36px;background:var(--green);color:var(--white);font-size:21px;padding:4px 22px}
.link-cols{display:flex;gap:40px;padding:12px 24px}
.link-list{list-style:none;font-size:14px;line-height:29px;color:#222}
.link-list li::before{content:"";display:inline-block;width:0;height:0;border-left:5px solid #333;border-top:4px solid transparent;border-bottom:4px solid transparent;margin-right:8px}

/* footer */
.site-footer{left:0;top:2060px;width:1200px;height:269px;background:var(--navy)}
.footer-col{top:2090px;width:150px}
.footer-head{font-size:14px;color:var(--white);line-height:17px;margin-bottom:6px}
.footer-list{list-style:none;font-size:11.5px;line-height:15px;color:var(--footer-text)}
.footer-brand{left:845px;top:2086px;width:164px;height:52px;background:var(--white);display:flex;align-items:center;justify-content:center;gap:6px;font-weight:800;font-size:13px;color:var(--navy)}
.footer-brand-mark{width:10px;height:10px;background:var(--navy)}
.footer-address{left:852px;top:2166px;font-size:11px;line-height:14px;color:var(--footer-text);width:200px;font-style:normal}
.footer-address strong{color:var(--white);font-weight:700}
.copyright{left:0;top:2329px;width:1200px;height:38px;font-size:12px;color:#333;display:flex;align-items:center;justify-content:center}
</style>
</head>
<body>

<header class="abs site-header">
  <div class="abs brand"><span class="brand-mark"></span><span class="brand-name">BRELLIN TRADE PARTNERS</span></div>
  <div class="abs header-phone">
    <svg width="20" height="20" viewBox="0 0 24 24" aria-hidden="true"><circle cx="12" cy="12" r="12" fill="#111"/><path d="M8.5 6.5c.5-.3 1 0 1.3.5l1 1.8c.2.5.1 1-.3 1.3l-.8.6c.6 1.3 1.6 2.3 2.9 2.9l.6-.8c.3-.4.8-.5 1.3-.3l1.8 1c.5.3.8.8.5 1.3-.6 1.2-1.8 1.7-3 1.3-3-1-5.3-3.3-6.3-6.3-.4-1.2.1-2.4 1-3.3z" fill="#fff"/></svg>
    555-014-2200
  </div>
</header>

<nav class="abs main-nav">
  <ul class="nav-list">
    <li class="is-active">Home</li>
    <li>About Us</li>
    <li>Product Categories</li>
    <li>Request A Quote</li>
    <li>Blog</li>
    <li>Contact Us</li>
  </ul>
</nav>

<div class="abs hero-photo" role="img" aria-label="Workers in green smocks at rows of sewing machines on a garment factory floor"></div>
<div class="abs hero-caption">Asian Outsourcing<br>Made Easy!</div>

<section class="abs intro-band"></section>
<h2 class="abs section-title intro-title">SOURCE YOUR GOODS RIGHT NOW !</h2>
<p class="abs intro-copy">We outsource sewing services direct from China. Our long-established and extensive network of offshore factory-partners provides our clients with access to a wide variety of contract sewing expertise from Chinese manufacturers. Clients only need to communicate with our US agents, but will have the benefits of the cost savings &amp; quality workmanship from offshore outsourcing from Asia.</p>
<div class="abs video-frame">
  <div class="abs video-still" role="img" aria-label="Video still of sewing workers at machines in a factory"></div>
  <div class="abs video-title">Factory Tour Video</div>
  <div class="abs video-play"><svg width="60" height="60" viewBox="0 0 60 60" aria-hidden="true"><path d="M24 18l18 12-18 12z" fill="#fff"/></svg></div>
  <div class="abs video-controls"><div class="abs video-progress"></div></div>
</div>

<h2 class="abs section-title sourcing-title">SOURCING CUSTOM GOODS IN CHINA</h2>
<p class="abs sourcing-copy">We outsource sewing services direct from China. Our long-established and extensive network of offshore factory-partners provides our clients with access to a wide variety of contract sewing expertise from Chinese manufacturers. Clients only need to communicate with our US-agents, but will have the benefits of the cost savings &amp; quality workmanship from offshore outsourcing from Asia.</p>

<div class="abs product-card" style="left:163px;top:914px"><div class="product-photo" role="img" aria-label="Hands guiding red fabric through a sewing machine" style="background:radial-gradient(circle at 40% 60%,#c0392b,transparent 45%),linear-gradient(135deg,#d8b08c,#8a5a3a)"></div><div class="product-label">Sewn Goods</div></div>
<div class="abs product-card" style="left:396px;top:914px"><div class="product-photo" role="img" aria-label="Grey and red messenger bag" style="background:radial-gradient(ellipse 60px 50px at 50% 55%,#b22,transparent 70%),linear-gradient(#fff 10%,#666 40%,#444 75%,#fff 95%)"></div><div class="product-label">Bags</div></div>
<div class="abs product-card" style="left:611px;top:914px"><div class="product-photo" role="img" aria-label="Pair of black and white work gloves" style="background:radial-gradient(ellipse 40px 60px at 35% 50%,#222,transparent 70%),radial-gradient(ellipse 40px 60px at 68% 55%,#ccc,transparent 70%),#fafafa"></div><div class="product-label">Gloves</div></div>
<div class="abs product-card" style="left:833px;top:914px"><div class="product-photo" role="img" aria-label="Blue motorcycle cover" style="background:radial-gradient(ellipse 90px 60px at 50% 55%,#26358f,transparent 75%),linear-gradient(#fafafa,#e8e8ee)"></div><div class="product-label">Covers</div></div>
<div class="abs product-card" style="left:163px;top:1160px"><div class="product-photo" role="img" aria-label="Row of colourful phone cases" style="background:linear-gradient(90deg,#fff 8%,#2e3fa8 8%,#2e3fa8 26%,#5a3fb0 26%,#5a3fb0 44%,#8a3aa8 44%,#8a3aa8 62%,#c23a8a 62%,#c23a8a 80%,#fff 80%)"></div><div class="product-label">Cases</div></div>
<div class="abs product-card" style="left:396px;top:1160px"><div class="product-photo" role="img" aria-label="Quilted light blue medical pad" style="background:radial-gradient(ellipse 70px 45px at 50% 50%,#c7d6ef,transparent 80%),#f6f8fc"></div><div class="product-label">Medical</div></div>
<div class="abs product-card" style="left:611px;top:1160px"><div class="product-photo" role="img" aria-label="Red, white and black golf bags" style="background:radial-gradient(ellipse 70px 55px at 50% 45%,#c02a2a,transparent 75%),linear-gradient(#fafafa 20%,#333 90%)"></div><div class="product-label">Sporting Goods</div></div>

<section class="abs contact-band"></section>
<p class="abs contact-lead">Please contact us for immediate consultation regarding your outsourcing project.</p>
<p class="abs contact-lines">Tel: 555-014-2200<br>Fax: 555-014-2201<br>Email: info@brellintrade.example</p>
<form class="abs quote-form">
  <div class="quote-head">REQUEST A QUOTE</div>
  <div class="quote-field" style="top:64px">Name:</div>
  <div class="quote-field" style="top:108px">Email:</div>
  <div class="quote-field" style="top:152px">Phone:</div>
  <div class="quote-field" style="top:196px;height:74px">Comment:</div>
  <div class="quote-submit">Submit</div>
</form>

<div class="abs link-panel" style="left:165px">
  <div class="link-head">SOURCING SOLUTIONS</div>
  <div class="link-cols">
    <ul class="link-list" style="width:130px"><li>Bags</li><li>Cases</li><li>Covers</li><li>Gloves</li><li>Medical</li></ul>
    <ul class="link-list"><li>Sewn Goods</li><li>Sporting Goods</li></ul>
  </div>
</div>
<div class="abs link-panel" style="left:611px">
  <div class="link-head">WHAT YOU NEED TO KNOW</div>
  <div class="link-cols">
    <ul class="link-list"><li>Contract Sewing in China</li><li>What is the Process?</li><li>What the Minimum Order?</li><li>Contract Outsourcing FAQ</li><li>Outsourcing Case Study</li><li>Custom Industrial Sewing in China</li></ul>
  </div>
</div>

<footer class="abs site-footer"></footer>
<div class="abs footer-col" style="left:185px">
  <div class="footer-head">CUSTOM BAGS</div>
  <ul class="footer-list"><li>Athletic Bags</li><li>Backpacks</li><li>Computer Bags</li><li>Cooler Bags</li><li>Cosmetic Bags</li><li>Handbags</li><li>Messenger Bags</li><li>Shopping Bags</li><li>Tool Bags</li><li>Travel Bags</li><li>Yoga Bags</li></ul>
</div>
<div class="abs footer-col" style="left:310px">
  <div class="footer-head">CUSTOM COVERS</div>
  <ul class="footer-list"><li>ATV Covers</li><li>Chair Covers</li><li>Dust/Sheet Covers</li><li>Golf Cart Covers</li><li>Motorcycle Covers</li><li>Outdoor Furniture Covers</li><li>Outdoor Grill Cover</li><li>Personal Water-craft Covers</li></ul>
</div>
<div class="abs footer-col" style="left:466px">
  <div class="footer-head">CUSTOM MEDICAL ACCESSORIES</div>
  <ul class="footer-list"><li>Medical Equipment Covers</li><li>Medical Pads</li><li>Medical Sheets &amp; Bedding Supplies</li><li>Oxygen Tank Cases and Bags</li></ul>
</div>
<div class="abs footer-col" style="left:632px">
  <div class="footer-head">CUSTOM SEWN GOODS</div>
  <ul class="footer-list"><li>Pet Collars, Leashes, &amp; Harnesses</li><li>Socks</li></ul>
  <div class="footer-head" style="margin-top:12px">CUSTOM CASES</div>
  <ul class="footer-list"><li>Cosmetic Cases</li><li>Phone Cases</li><li>Tool Bags and Tool Cases</li></ul>
</div>
<div class="abs footer-brand"><span class="footer-brand-mark"></span>BRELLIN TRADE</div>
<address class="abs footer-address">
  <strong>US HEADQUARTERS</strong><br><br>
  <strong>Brellin Trade Partners</strong><br>
  48 Lindell Road<br>Unit 3<br>Dorset, NH 03000<br><br>
  Online Inquiry Form<br>Tel: 555-014-2200<br>Fax: 555-014-2201<br>Email: info@brellintrade.example
</address>
<div class="abs copyright">Copyright © 2015 Brellin Trade</div>

</body>
</html>
```